Design some Business Cards for Kelvara

A startup company named Kelvara IT is looking for a business card design. It needs to be modern, with a strong sense of professionalism and creativity. Design would need to be both front and back. No costs will be spared during printing, so incorporate any printing styles, embossing etc. Size needs to be the standard card size.

The design needs to incorporate the logo provided, include phone number, email address, job title, and company website.

Company website is [login to view URL]

Cards would be for:

Miles Harrow
CEO
Miles@kelvara-mail.example
555-402-3391

Pat Lowry
COO/CIO
Pat@kelvara-mail.example
555-739-1046

Tom Vallerup
V.P. of Design
Tom@kelvara-mail.example
555-158-6627

Dana Whitby
V.P. of Sales
Dana@kelvara-mail.example
555-823-9570

```html
<!DOCTYPE html>
<html lang="en">
<head>
<meta charset="utf-8">
<title>Kelvara IT — Business Card</title>
<link rel="stylesheet" href="https://fonts.googleapis.com/css2?family=Open+Sans:wght@400;600;700&display=swap">
<style>
  :root {
    --backdrop: #bcbdbf;
    --brand-blue: #0aa4df;
    --charcoal: #3e3e43;
    --paper: #ffffff;
  }
  * { margin: 0; padding: 0; box-sizing: border-box; }
  html, body { width: 1200px; height: 839px; overflow: hidden; }
  body {
    background: var(--backdrop);
    font-family: "Open Sans", Arial, sans-serif;
    position: relative;
  }
  .card {
    position: absolute;
    top: 104px;
    width: 406px;
    height: 631px;
    border-radius: 18px;
    overflow: hidden;
  }
  .card--front { left: 157px; }
  .card--back { left: 635px; background: var(--brand-blue); }
  .card__shapes { position: absolute; inset: 0; display: block; }
  .holder {
    position: absolute;
    left: 0; right: 0;
    text-align: center;
  }
  .holder__name {
    top: 30px;
    color: var(--paper);
    font-weight: 700;
    font-size: 22px;
  }
  .holder__title {
    top: 62px;
    color: var(--charcoal);
    font-weight: 400;
    font-size: 18px;
  }
  .wordmark {
    position: absolute;
    left: 0; right: 0;
    text-align: center;
    font-weight: 700;
    letter-spacing: -0.5px;
    line-height: 1;
  }
  .card--front .wordmark { top: 214px; font-size: 58px; color: var(--charcoal); }
  .card--back .wordmark { top: 285px; font-size: 58px; color: var(--paper); }
  .contacts {
    position: absolute;
    left: 118px;
    top: 480px;
    list-style: none;
    color: var(--paper);
    font-size: 19px;
  }
  .contacts__item {
    display: flex;
    align-items: center;
    height: 38px;
  }
  .contacts__icon {
    width: 18px; height: 18px;
    margin-right: 12px;
    flex: none;
  }
</style>
</head>
<body>
  <section class="card card--front" aria-label="Card front">
    <svg class="card__shapes" viewBox="0 0 406 631" aria-hidden="true">
      <rect width="406" height="631" fill="var(--charcoal)"/>
      <rect width="406" height="22" fill="var(--brand-blue)"/>
      <path d="M88,18 C102,18 106,28 107,42 L107,86 Q107,94 116,94 L290,94 Q299,94 299,86 L299,42 C300,28 304,18 318,18 Z" fill="var(--brand-blue)"/>
      <rect y="100" width="406" height="283" fill="var(--paper)"/>
      <polygon points="0,383 406,383 406,400 203,427 0,400" fill="var(--brand-blue)"/>
    </svg>
    <p class="holder holder__name">Miles Harrow</p>
    <p class="holder holder__title">CEO</p>
    <p class="wordmark">Kelvara IT</p>
    <ul class="contacts">
      <li class="contacts__item">
        <svg class="contacts__icon" viewBox="0 0 18 18" aria-hidden="true">
          <rect width="18" height="18" rx="3" fill="var(--paper)"/>
          <path d="M4,7 Q9,3 14,7 L13,9 L11,8 L11,7 Q9,6 7,7 L7,8 L5,9 Z" fill="var(--charcoal)"/>
          <rect x="5" y="10" width="8" height="4" rx="1" fill="var(--charcoal)"/>
        </svg>
        <span>555-402-3391</span>
      </li>
      <li class="contacts__item">
        <svg class="contacts__icon" viewBox="0 0 18 18" aria-hidden="true">
          <rect width="18" height="18" rx="3" fill="var(--paper)"/>
          <rect x="3" y="5" width="12" height="8" fill="var(--charcoal)"/>
          <path d="M3,5 L9,10 L15,5" fill="none" stroke="var(--paper)" stroke-width="1.2"/>
        </svg>
        <span>Miles@kelvara-mail.example</span>
      </li>
      <li class="contacts__item">
        <svg class="contacts__icon" viewBox="0 0 18 18" aria-hidden="true">
          <rect width="18" height="18" rx="3" fill="var(--paper)"/>
          <circle cx="9" cy="9" r="5.5" fill="none" stroke="var(--charcoal)" stroke-width="1.2"/>
          <ellipse cx="9" cy="9" rx="2.4" ry="5.5" fill="none" stroke="var(--charcoal)" stroke-width="1"/>
          <line x1="3.5" y1="9" x2="14.5" y2="9" stroke="var(--charcoal)" stroke-width="1"/>
        </svg>
        <span>www.kelvara.example</span>
      </li>
    </ul>
  </section>

  <section class="card card--back" aria-label="Card back">
    <p class="wordmark">Kelvara IT</p>
  </section>
</body>
</html>
```